Nanny Share Ecommerce Website for Finding Childcare and Parents who need Childcare HuggaSitter.com

Our company needs an ecommerce website (HuggaSitter.com) for a US subscription based service strictly for nanny sharing that connects families and caregivers. The website would allow families to connect with one another as well as to search for nannies. The service would be searchable for other families by location (by radius or zip code), children demographic (age range/gender/special needs), days of week or times, after school care, school closure days (holidays), etc. The service would also be searchable for nannies based on gender, provider age range, years experience, language, hourly rate, transportation available, certification (CPR first aid), education etc. The search fields would be searchable and sortable and allow to connect with the provider (after paying subscription fee). The service would be similar to tendly.com in that it would allow for families and caregivers to post photos as well as a short bio of the themselves. There would also be a feedback/star rating mechanism to rate caregivers who have performed work for families (viewable to public). The service would be free for nannies to post their bios and only a subscription based service for families to connect with other families or with caregivers (able to view bio but need service to connect). There will be a short bio on the benefits of nanny sharing (reduced cost, increased flexibility for parents, reduced illness, increased socialization with other children vs. sole nanny), as well as Q&A section with best practices.

Target Market(s)

Families, Nannies

Industry/Entity Type

Childcare

Logo Text

Hugga Sitter

Coding

Coded - Design and coding required

Number of Pages Required

5+ page

Requirements
Must have
• Searchable (need to be able to search for families as well as nannies), responsive, functional, easy to use, add value to families and nannies. Needs to be able to collect payment for subscription.
Nice to have
• Optimized for mobile, SEO optimized

```html
<!DOCTYPE html>
<html lang="en">
<head>
<meta charset="utf-8">
<title>Hugga Sitter – Nanny Sharing for Families and Caregivers</title>
<link href="https://fonts.googleapis.com/css2?family=Lato:ital,wght@0,400;0,700;0,900;1,400&family=Open+Sans:ital,wght@0,400;0,600;0,700;1,400&display=swap" rel="stylesheet">
<style>
:root{
  --teal:#2c8096;
  --teal-dark:#236b7e;
  --teal-light:#74bccb;
  --teal-pale:#e6f3f6;
  --pink:#d9596d;
  --ink:#2a2a2a;
  --muted:#7a7a7a;
  --soft:#9a9a9a;
  --line:#dcdcdc;
  --grey:#efefef;
  --white:#fff;
}
*{box-sizing:border-box;margin:0;padding:0}
html,body{width:1200px;height:2885px;overflow:hidden}
body{font-family:"Open Sans",Arial,sans-serif;color:var(--ink);background:var(--white);position:relative}
h1,h2,h3,h4{font-family:"Lato",Arial,sans-serif}
a{color:inherit;text-decoration:none}

/* top bar + header */
.topbar{height:17px;background:var(--teal-light);display:flex;justify-content:flex-end;align-items:center;gap:14px;padding-right:220px;font-size:9px;color:var(--white)}
.header{height:55px;display:flex;align-items:center;justify-content:space-between;padding:0 206px 0 204px;border-bottom:1px solid var(--line)}
.brand{display:flex;align-items:center;gap:8px;margin-top:-22px;background:var(--white);padding:6px 10px;border-radius:0 0 8px 8px}
.brand-dot{width:22px;height:22px;border-radius:50%;background:var(--pink)}
.brand-name{font-family:"Lato",sans-serif;font-weight:900;font-size:22px;color:var(--teal)}
.nav{display:flex;gap:14px;align-items:center;font-size:10px;font-weight:700;text-transform:uppercase}
.nav .active{color:var(--pink)}
.search-btn{width:22px;height:22px;border:1px solid var(--pink);display:flex;align-items:center;justify-content:center}

/* hero */
.hero{position:absolute;top:72px;left:0;width:1200px;height:568px}
.hero-photo{position:absolute;inset:0;background:linear-gradient(100deg,#cfc7bf 0%,#b8aba0 35%,#8f7b6c 60%,#4a3b33 100%)}
.hero-title{position:absolute;left:200px;top:150px;color:var(--white);font-size:40px;font-weight:700;line-height:1.2}
.hero-title span{display:block;font-size:33px}
.option-box{position:absolute;left:288px;top:332px;width:548px;height:188px;background:var(--white);box-shadow:0 6px 14px rgba(0,0,0,.18);padding:14px 26px;text-align:center}
.option-box::before{content:"";position:absolute;inset:8px;border:1px solid var(--teal-light);pointer-events:none}
.option-lead{font-family:"Lato",sans-serif;font-style:italic;font-size:14px;margin-bottom:14px}
.options{display:flex;gap:30px;justify-content:center}
.option{width:215px}
.option h4{font-weight:400;font-size:13px;margin-bottom:6px}
.option h4 em{font-weight:700;font-size:16px}
.option p{border:1px solid var(--pink);font-size:9px;color:var(--soft);padding:8px 6px;height:50px}
.btn{display:inline-block;background:var(--pink);color:var(--white);font-size:11px;font-weight:700;padding:6px 18px;text-transform:uppercase}
.option .btn{margin-top:-12px;position:relative}

/* feature rows */
.feature{position:absolute;left:0;width:1200px;height:289px;display:flex}
.feature .photo{width:592px;height:100%}
.feature .copy{width:608px;padding:50px 40px 0 36px}
.feature h3{font-size:24px;font-weight:700;margin-bottom:12px}
.feature .lead{color:var(--teal-light);font-size:15px;line-height:1.35;margin-bottom:10px}
.feature .body{font-size:11px;color:var(--muted);line-height:1.6}
.matching{top:640px}
.matching .photo{background:linear-gradient(120deg,#e7d7c5,#c9a68a 50%,#8c6852)}
.finding{top:929px}
.finding .copy{padding:45px 30px 0 210px;width:592px}
.finding .photo{width:608px;background:linear-gradient(120deg,#f2f0ec,#d9cfc5 50%,#8f857a)}

/* why */
.why{position:absolute;top:1217px;left:0;width:1200px;height:364px;background:var(--teal);text-align:center;color:var(--white)}
.why::after{content:"";position:absolute;left:0;right:0;bottom:0;height:117px;background:var(--teal-light)}
.why h2{font-size:30px;font-weight:700;padding-top:42px}
.why .sub{font-size:11px;opacity:.85;width:400px;margin:8px auto 0;line-height:1.5}
.why-cards{position:absolute;left:216px;top:145px;width:771px;height:167px;background:var(--white);display:flex;z-index:1;color:var(--ink)}
.why-card{flex:1;border-right:1px solid var(--line);display:flex;flex-direction:column;align-items:center;padding-top:30px;font-size:12px;font-weight:700;line-height:1.3}
.why-card:last-child{border-right:0}
.why-card svg{width:56px;height:56px;margin-bottom:14px}
.why .more{position:absolute;left:0;right:0;bottom:12px;font-size:10px;letter-spacing:1px;z-index:1}

/* nannies */
.nannies{position:absolute;top:1581px;left:0;width:1200px;height:381px;text-align:center}
.nannies h2{font-size:26px;padding-top:52px}
.nannies .sub{font-size:11px;color:var(--muted);width:400px;margin:10px auto 0;line-height:1.5}
.carousel-arrow{position:absolute;top:216px;width:26px;height:26px;background:var(--grey);display:flex;align-items:center;justify-content:center}
.nanny-cards{position:absolute;top:179px;left:210px;display:flex;gap:6px}
.nanny-card{width:260px;height:110px;border:1px solid var(--teal-light);display:flex;padding:8px;text-align:left;gap:8px}
.nanny-photo{width:92px;height:92px;background:linear-gradient(135deg,#e9d2c2,#9d7a66)}
.nanny-info{flex:1;font-size:10px;color:var(--muted);position:relative}
.nanny-info h4{font-size:12px;color:var(--teal);font-weight:700}
.tag{position:absolute;right:0;top:0;border:1px solid var(--line);font-size:8px;padding:2px 6px}
.stars{color:#f2b01e;font-size:11px;letter-spacing:1px;margin:3px 0}
.nanny-info .btn{font-size:9px;padding:4px 8px;margin-top:8px}
.nanny-info .fav{font-size:9px;color:var(--teal);margin-left:6px}
.nannies .more{position:absolute;left:0;right:0;top:326px;font-size:10px;color:var(--pink);letter-spacing:1px}

/* testimonials */
.testimonials{position:absolute;top:1962px;left:0;width:1200px;height:389px;background:var(--grey)}
.testimonials .photo{position:absolute;left:0;top:0;width:505px;height:100%;background:linear-gradient(110deg,#f4ece4,#e4cdb8 50%,#c9a990)}
.testimonials h2{position:absolute;left:695px;top:55px;font-size:34px}
.testimonials .tag-line{position:absolute;left:690px;top:100px;font-style:italic;color:var(--teal-light);font-size:16px}
.quote-mark{position:absolute;left:502px;top:130px;font-family:"Lato",sans-serif;font-size:130px;color:var(--teal);line-height:1}
.testimonials .text{position:absolute;left:620px;top:150px;width:420px;text-align:center;font-size:11px;color:var(--muted);line-height:1.9}
.testimonials .author{position:absolute;left:745px;top:295px;font-size:11px;color:var(--pink)}
.slide-dots{position:absolute;left:745px;top:332px;display:flex;gap:4px}
.slide-dots span{width:22px;height:22px;background:var(--white);border:1px solid var(--line);display:flex;align-items:center;justify-content:center;font-size:10px}

/* query */
.query{position:absolute;top:2351px;left:0;width:1200px;height:309px;text-align:center}
.query h2{font-size:38px;padding-top:40px}
.query .dw{font-size:15px;font-weight:700;font-family:"Lato",sans-serif}
.query .sub{font-size:11px;color:var(--muted);width:470px;margin:26px auto 0;line-height:1.6}
.query-actions{position:absolute;left:360px;top:200px;display:flex;align-items:center}
.faq-btn{background:var(--teal);color:var(--white);font-size:10px;letter-spacing:1px;padding:10px 28px;width:210px}
.or{width:46px;height:46px;border-radius:50%;background:var(--pink);color:var(--white);font-weight:700;display:flex;align-items:center;justify-content:center;margin:0 -4px;z-index:1;font-size:16px}
.call{background:var(--teal);color:var(--white);font-size:18px;font-weight:700;padding:6px 22px;width:230px;font-family:"Lato",sans-serif}

/* footer */
.footer{position:absolute;top:2660px;left:0;width:1200px;height:196px;background:var(--teal);color:var(--white);display:flex;padding:38px 0 0 196px;gap:40px}
.footer .brand{margin:12px 20px 0 0;background:transparent;padding:0}
.footer .brand-name{color:var(--white);font-size:26px}
.fcol h5{font-size:10px;font-weight:700;text-transform:uppercase;margin-bottom:6px}
.fcol li{list-style:none;font-size:9px;line-height:1.65;opacity:.9}
.social{display:flex;gap:4px;margin-bottom:30px}
.social span{width:20px;height:20px;background:var(--white);opacity:.9}
.subscribe{border:2px solid var(--white);font-size:10px;font-weight:700;padding:8px 12px;display:inline-block}
.bottom{position:absolute;top:2856px;left:0;width:1200px;height:29px;background:var(--teal-dark);color:var(--white);font-size:9px;display:flex;justify-content:space-between;align-items:center;padding:0 210px 0 196px}
.bottom nav{display:flex;gap:14px}
</style>
</head>
<body>

<div class="topbar"><a>Login</a><a>Join Now</a><a>For Members</a><a>Change Country</a></div>
<header class="header">
  <div class="brand"><span class="brand-dot"></span><span class="brand-name">Hugga Sitter</span></div>
  <nav class="nav">
    <a class="active">Home</a><a>About Us</a><a>Our Services</a><a>Our Benefits</a><a>FAQ</a><a>Contact Us</a>
    <span class="search-btn"><svg width="11" height="11" viewBox="0 0 12 12"><circle cx="5" cy="5" r="3.8" fill="none" stroke="#d9596d" stroke-width="1.5"/><line x1="8" y1="8" x2="11" y2="11" stroke="#d9596d" stroke-width="1.5"/></svg></span>
  </nav>
</header>

<section class="hero">
  <div class="hero-photo" role="img" aria-label="Photo of a smiling mother holding her young child indoors"></div>
  <h1 class="hero-title">Trusted by families.<span>Loved by caregivers.</span></h1>
  <div class="option-box">
    <p class="option-lead">Let's get Started. Choose an option.</p>
    <div class="options">
      <div class="option">
        <h4>I need a <em>Caregiver</em></h4>
        <p>Start your free search for care in your area.</p>
        <a class="btn">Find Care</a>
      </div>
      <div class="option">
        <h4>I want a <em>Care Job</em></h4>
        <p>Create a free profile and search for jobs.</p>
        <a class="btn">Find Jobs</a>
      </div>
    </div>
  </div>
</section>

<section class="feature matching">
  <div class="photo" role="img" aria-label="Photo of a happy family with parents and three children"></div>
  <div class="copy">
    <h3>Matching Families</h3>
    <p class="lead">We know that finding a family to share your caregiver is just as important as finding a nanny.</p>
    <p class="body">That's why we specialize in helping you find local families that are looking for the same personalized care. You'll have the ability to search for families by the age range of children, gender, location, days or times of the week, as well as other personalized preferences for that perfect family.</p>
  </div>
</section>

<section class="feature finding">
  <div class="copy">
    <h3>Finding Caregivers</h3>
    <p class="lead">Once you've found the perfect family to share your caregiver we recommend you start your search for a nanny that meets your personalized needs.</p>
    <p class="body">Search for the perfect caregiver by education and experience, location, salary, certifications, and other qualifications. We'll ensure that you and the families you partner with find the perfect caregiver to complement your personalized care needs.</p>
  </div>
  <div class="photo" role="img" aria-label="Photo of a caregiver playing with a baby on a rug"></div>
</section>

<section class="why">
  <h2>Why choose Hugga Sitter</h2>
  <p class="sub">Families share one trusted caregiver, split the cost and give children friends to grow with every day.</p>
  <div class="why-cards">
    <div class="why-card">
      <svg viewBox="0 0 56 56" fill="none" stroke="#d9596d" stroke-width="2"><rect x="10" y="18" width="36" height="26" rx="3"/><circle cx="28" cy="31" r="6"/><path d="M18 18l10-8 10 8"/></svg>
      Reduced Cost
    </div>
    <div class="why-card">
      <svg viewBox="0 0 56 56" fill="none" stroke="#d9596d" stroke-width="2"><circle cx="19" cy="16" r="5"/><circle cx="37" cy="16" r="5"/><path d="M11 46V28a8 8 0 0 1 16 0v18M29 46V28a8 8 0 0 1 16 0v18"/></svg>
      Increased Flexibility<br>for Parents
    </div>
    <div class="why-card">
      <svg viewBox="0 0 56 56" fill="none" stroke="#d9596d" stroke-width="2"><circle cx="28" cy="28" r="18"/><circle cx="22" cy="24" r="2"/><circle cx="34" cy="24" r="2"/><path d="M21 34q7 5 14 0"/></svg>
      Reduced Illness
    </div>
    <div class="why-card">
      <svg viewBox="0 0 56 56" fill="none" stroke="#d9596d" stroke-width="2"><circle cx="16" cy="28" r="5"/><circle cx="40" cy="14" r="5"/><circle cx="40" cy="42" r="5"/><path d="M21 26l14-10M21 30l14 10"/></svg>
      Increased<br>Socialization
    </div>
    <div class="why-card">
      <svg viewBox="0 0 56 56" fill="none" stroke="#d9596d" stroke-width="2"><circle cx="28" cy="18" r="8"/><path d="M14 46a14 14 0 0 1 28 0z"/><path d="M24 30l4 5 4-5"/></svg>
      We Are More Than<br>Just a Nanny Agency
    </div>
  </div>
  <a class="more">CLICK HERE KNOW MORE</a>
</section>

<section class="nannies">
  <h2>Our Top Rated Nannies</h2>
  <p class="sub">Caregivers rated highly by the families they have worked with, with reviews open to everyone.</p>
  <span class="carousel-arrow" style="left:152px"><svg width="8" height="10" viewBox="0 0 8 10"><path d="M6 1L2 5l4 4" fill="none" stroke="#777" stroke-width="1.5"/></svg></span>
  <span class="carousel-arrow" style="left:1010px"><svg width="8" height="10" viewBox="0 0 8 10"><path d="M2 1l4 4-4 4" fill="none" stroke="#777" stroke-width="1.5"/></svg></span>
  <div class="nanny-cards">
    <div class="nanny-card">
      <div class="nanny-photo" role="img" aria-label="Profile photo of nanny Rosa M."></div>
      <div class="nanny-info"><span class="tag">Welcome</span><h4>Rosa M.</h4><div class="stars">★★★★★</div>Cared for 4 families<br><a class="btn">Send Message</a><span class="fav">+ Saved</span></div>
    </div>
    <div class="nanny-card">
      <div class="nanny-photo" role="img" aria-label="Profile photo of nanny Kelsey"></div>
      <div class="nanny-info"><span class="tag">Welcome</span><h4>Kelsey</h4><div class="stars">★★★★★</div>Cared for 3 families<br><a class="btn">Send Message</a><span class="fav">+ Saved</span></div>
    </div>
    <div class="nanny-card">
      <div class="nanny-photo" role="img" aria-label="Profile photo of nanny Nina T."></div>
      <div class="nanny-info"><span class="tag">Welcome</span><h4>Nina T.</h4><div class="stars">★★★★★</div>Cared for 5 families<br><a class="btn">Send Message</a><span class="fav">+ Saved</span></div>
    </div>
  </div>
  <a class="more">CLICK HERE TO VIEW ALL</a>
</section>

<section class="testimonials">
  <div class="photo" role="img" aria-label="Photo of a smiling mother with her baby"></div>
  <h2>Testimonials</h2>
  <p class="tag-line">Few words from happy parents</p>
  <div class="quote-mark">“</div>
  <p class="text">Sharing one nanny with the family down the street changed our weeks. We split the cost, our kids play together every day and we both have flexible hours again. The search made it easy to find parents with the same schedule and a caregiver we trust completely. We could not be happier with the match.</p>
  <p class="author">Dana Whitlow</p>
  <div class="slide-dots"><span>‹</span><span>›</span></div>
</section>

<section class="query">
  <h2>Still you have query ?</h2>
  <p class="dw">Don't worry &nbsp;we are here</p>
  <p class="sub">Read our answers and best practices on nanny sharing, or call our team for help choosing a plan.</p>
  <div class="query-actions">
    <a class="faq-btn">FREQUENTLY ASKED QUESTIONS</a>
    <span class="or">OR</span>
    <a class="call">CALL US: +1 555 014 2290</a>
  </div>
</section>

<footer class="footer">
  <div class="brand"><span class="brand-dot"></span><span class="brand-name">Hugga Sitter</span></div>
  <div class="fcol"><h5>Company</h5><ul><li>About Us</li><li>Investor Relations</li><li>Membership</li><li>Blog</li><li>Safety Center</li><li>Careers</li></ul></div>
  <div class="fcol"><h5>Popular Topics</h5><ul><li>Babysitters</li><li>Nannies</li><li>Child Care</li><li>Housekeepers</li><li>Tutors</li></ul></div>
  <div class="fcol"><h5>Our Services</h5><ul><li>Matching Families</li><li>Finding Caregivers</li></ul></div>
  <div class="fcol"><h5>Join Us</h5><div class="social"><span></span><span></span><span></span><span></span><span></span></div><a class="subscribe">SUBSCRIBE US NOW</a></div>
</footer>
<div class="bottom">
  <nav><a>Home</a><a>About Us</a><a>Our Services</a><a>Our Benefits</a><a>FAQ</a><a>Contact Us</a></nav>
  <span>© 2017-2018 HuggaSitter.com. All Rights Reserved.</span>
</div>

</body>
</html>
```